Design Car Sharing App Mockups

What do we do?
We are a car sharing company. One of the main functionality of our product is a driver’s app which allows our customers to reserve a car and manage the car doors without a car key. Our website is www.velmora.fi.

What do we need?
We need a new UI design for this driver's app.

For this task we are expecting 6 app pages / screen views:
1) A view showing what it could look like to search for and reserve a car
2) An example of what a UI pop-up could look like for this app (e.g., requesting more time with an on-going reservation)
3) An example of what a page would look like for seeing existing bookings or modifying them
4) An example of what the app would show when a car is actively booked and the driver is able to open and close the car doors
5) An example of how the driver's renter history could be displayed
6) One additional page to show off your own intuition with the app (e.g., a menu screen, reporting damage screen, etc.)

You can test an old (demo) version of the app here:
http://velmoradev.quillhost.net:8080/bdriver/
(In the login view just press ‘Sign in’. The contents of the ‘Email’ or ‘Password’ fields does not matter.
In the ‘Book’ view just press the figure above ‘Book a time’ text to open the calendar view.)

For a clearer note on the elements we want to see on the page and technical requirements, see below:
Technical specification of the required views/view components:
- Menu
- Searching and reserving cars based on time and duration criteria
- Managing your car reservations (delete, edit)
(Editing is not possible in the old app.)
- When you have an ongoing reservation, it should be possible to:
Open and close car doors
Request more time before you have to return the car (Sometimes it is possible, sometimes not).
- Browsing through your driving history
- Optional page view: Future reservations should show when your reservations is:
About to start
About to end
Has ended without you checking out(returning) the car.
- It shows when you have ‘checked in’ into an ongoing reservation
(Checking in makes opening&closing car doors possible).
- When you have an ongoing reservation there should be a button such as 'Report issue" or something like that for situations when you notice a scratch
or something else alarming in the condition of the car.
You don't need to create the actual view for making a car condition report, only the button for going there.
(This functionality is not in the old app.)
- Reservations/past uses paid with a private card are shown differently compared reservations/past uses paid with a company card.

```html
<!DOCTYPE html>
<html lang="en">
<head>
<meta charset="utf-8">
<title>Velmora Driver – App Screens</title>
<link href="https://fonts.googleapis.com/css2?family=Roboto:wght@300;400;500;700&display=swap" rel="stylesheet">
<style>
:root{
  --teal:#2bbcd4;
  --teal-dark:#1fa9c1;
  --blue:#1d6fc4;
  --red:#d8272e;
  --green:#35a84a;
  --orange:#f2a33a;
  --ink:#2b2f33;
  --muted:#8a9096;
  --line:#e3e6e8;
  --panel:#ffffff;
  --page:#ffffff;
  --screen-bg:#f1f2f3;
  --photo-car:linear-gradient(180deg,#6f87a1 0%,#a4b3c2 38%,#3a4047 62%,#1d2024 100%);
  --photo-dash:linear-gradient(180deg,#3a3e45 0%,#1f2126 55%,#121316 100%);
}
*{box-sizing:border-box;margin:0;padding:0}
html,body{width:1200px;height:851px;overflow:hidden;background:var(--page)}
body{position:relative;font-family:"Roboto",Arial,sans-serif;color:var(--ink)}

.screen{position:absolute;width:206px;height:364px;background:var(--screen-bg);overflow:hidden;box-shadow:0 0 0 1px #e6e6e6}
.row-top{top:48px}.row-bottom{top:450px}
.c1{left:40px}.c2{left:269px}.c3{left:498px}.c4{left:727px}.c5{left:956px}

.status{position:absolute;top:0;left:0;right:0;height:12px;font-size:6px;color:#fff;display:flex;justify-content:space-between;align-items:center;padding:0 6px;z-index:3}
.status .time{font-weight:500}

.appbar{position:absolute;top:0;left:0;right:0;height:45px;background:var(--teal);color:#fff}
.appbar .title{position:absolute;top:18px;left:0;right:0;text-align:center;font-size:10px}
.appbar .sub{position:absolute;left:0;right:0;text-align:center;font-size:9.5px;line-height:11px}
.appbar .icon{position:absolute}

.photo{position:absolute;left:0;right:0;top:0}
.round-btn{position:absolute;left:9px;top:22px;width:22px;height:22px;border-radius:50%;background:var(--teal);display:flex;align-items:center;justify-content:center}

.card{position:absolute;background:var(--panel);border-radius:3px;box-shadow:0 1px 4px rgba(0,0,0,.18)}
.pill{position:absolute;left:43px;width:120px;height:24px;border-radius:12px;color:#fff;font-size:8px;font-weight:500;letter-spacing:.3px;display:flex;align-items:center;justify-content:center}
.pill.teal{background:var(--teal)}
.pill.red{background:var(--red)}

/* Booking form */
.book-card{left:15px;top:210px;width:177px;height:153px}
.book-card h2{font-size:10px;font-weight:500;text-align:center;margin-top:12px}
.book-card .rule{height:1px;background:var(--line);margin:8px 0}
.label{font-size:6.5px;color:var(--teal);text-align:center;letter-spacing:.3px}
.value{font-size:10px;color:var(--muted);text-align:center;font-weight:300}
.split{display:flex;justify-content:space-around;margin-top:6px}
.split .cap{font-size:6.5px;color:var(--ink)}
.split .v{font-size:10px;color:var(--muted);font-weight:300;margin-top:2px}

/* Car list rows */
.car-row{position:absolute;left:3px;right:3px;height:64px;background:#fff;box-shadow:0 1px 2px rgba(0,0,0,.14)}
.thumb{position:absolute;left:0;top:0;bottom:0;width:76px;background:var(--photo-car)}
.car-row .info{position:absolute;left:82px;top:8px;right:6px}
.car-row .name{font-size:8.5px;font-weight:500}
.car-row .meta{font-size:6px;color:var(--muted);margin-top:1px}
.car-row .date{font-size:6px;color:var(--muted);margin-bottom:3px}
.car-row .price{font-size:8.5px;font-weight:500;margin-top:2px}
.avail{position:absolute;left:82px;bottom:16px;font-size:6px;color:var(--green);font-weight:500}
.mini{position:absolute;right:7px;bottom:10px;width:38px;height:14px;border-radius:7px;font-size:6px;color:#fff;font-weight:500;display:flex;align-items:center;justify-content:center}
.mini.drive{background:var(--blue)}
.mini.book{background:var(--teal)}
.tag{position:absolute;right:7px;bottom:9px;height:12px;padding:0 6px;border-radius:6px;border:1px solid;font-size:5.5px;font-weight:500;display:flex;align-items:center}
.tag.ongoing{color:var(--green);border-color:var(--green)}
.tag.complete{color:var(--teal);border-color:var(--teal)}
.tag.canceled{color:var(--red);border-color:var(--red)}

/* Car detail */
.detail-card{left:15px;top:165px;width:177px;height:151px;padding:9px 10px}
.detail-card .head{display:flex;justify-content:space-between}
.detail-card .nm{font-size:12px;font-weight:700}
.detail-card .sr{font-size:6.5px;color:var(--muted)}
.detail-card .pr{font-size:11px;color:var(--teal);text-align:right}
.detail-card .hr{font-size:6.5px;color:var(--teal);text-align:right}
.specs{display:grid;grid-template-columns:1fr 1fr;gap:7px 0;margin:9px 0 10px;font-size:8px}
.specs span{display:flex;align-items:center;gap:6px}
.detail-card p{font-size:6.5px;line-height:9px;color:#555}
.dots{position:absolute;top:188px;left:0;right:0;display:flex;justify-content:center;gap:3px}
.dots i{width:3px;height:3px;border-radius:50%;background:rgba(255,255,255,.5)}
.dots i:first-child{background:#fff}

/* Active reservation */
.active-card{left:15px;top:160px;width:177px;height:155px}
.active-card .nm{position:absolute;left:8px;top:10px;font-size:12px;font-weight:700}
.active-card .rem{position:absolute;left:8px;top:26px;font-size:6.5px;color:#555;line-height:8px}
.active-card .loc{position:absolute;left:8px;top:48px;font-size:5.5px;font-weight:500}
.lock{position:absolute;top:10px;width:22px;height:22px;border-radius:50%;display:flex;align-items:center;justify-content:center}
.lock.close{right:34px;background:var(--red)}
.lock.open{right:8px;background:var(--green)}
.map{position:absolute;left:0;right:0;bottom:0;height:96px;background:linear-gradient(135deg,#eceeed,#e2e5e3);border-radius:0 0 3px 3px}

/* Menu drawer */
.drawer{position:absolute;left:0;top:0;bottom:0;width:164px;background:#fff;z-index:2}
.drawer-shade{position:absolute;left:164px;top:0;right:0;bottom:0;background:linear-gradient(180deg,#4a4f55,#6c7176 50%,#3d4145)}
.avatar{position:absolute;left:16px;top:40px;width:45px;height:45px;border-radius:50%;background:linear-gradient(160deg,#c9b6a6,#6a5c52)}
.profile-name{position:absolute;left:73px;top:46px;font-size:11px}
.profile-link{position:absolute;left:73px;top:64px;height:13px;padding:0 7px;border:1px solid var(--teal);border-radius:7px;color:var(--teal);font-size:5.5px;font-weight:500;display:flex;align-items:center}
.drawer .rule{position:absolute;left:16px;right:12px;top:101px;height:1px;background:var(--line)}
.menu-item{position:absolute;left:20px;display:flex;align-items:center;gap:9px;font-size:8.5px;color:#444}
.menu-item.on{color:var(--teal)}
.menu-item svg{width:11px;height:11px}

/* Reservations swipe */
.swipe-actions{position:absolute;left:3px;right:3px;height:64px;background:#eceeef}
.swipe-card{position:absolute;left:0;top:0;width:130px;height:64px;background:#fff;box-shadow:1px 0 3px rgba(0,0,0,.15);padding:8px 10px}
.act{position:absolute;top:18px;font-size:6px;text-align:center;width:24px}
.act svg{display:block;margin:0 auto 3px}

/* Payment */
.pay-head{position:absolute;top:0;left:0;right:0;height:45px;background:var(--teal);color:#fff;font-size:10px}
.pay-head .cancel{position:absolute;left:9px;top:20px}
.pay-head .title{position:absolute;left:0;right:0;top:20px;text-align:center}
.pay-body{position:absolute;top:45px;left:0;right:0;bottom:0;background:#fff}
.pay-body h3{font-size:8.5px;font-weight:400;margin:14px 0 0 9px}
.tile{position:absolute;width:90px;height:66px;background:#eef0f1;text-align:center;font-size:6.5px}
.tile .art{width:50px;height:28px;margin:10px auto 4px;border-radius:3px}
.tile small{display:block;font-size:6px;color:#555}
.tile.selected{border:1.5px solid var(--blue);background:#eaf1fa}

/* Modal */
.scrim{position:absolute;inset:0;background:rgba(40,44,48,.55);z-index:2}
.modal{position:absolute;left:5px;width:195px;background:#fff;border-radius:4px;z-index:4;text-align:center;box-shadow:0 2px 10px rgba(0,0,0,.3)}
.modal .lead{font-size:8.5px;margin-top:10px}
.modal .carpic{width:40px;height:40px;border-radius:50%;background:var(--photo-car);margin:6px auto 5px}
.modal .nm{font-size:10px}
.modal .phase{font-size:9px;color:var(--teal);margin:9px 0 7px}
.modal .dt{display:flex;text-align:left;padding:0 23px}
.modal .dt div{flex:1}
.modal .dt .cap{font-size:5.5px;color:var(--muted)}
.modal .dt .v{font-size:9px;margin-top:2px}
.modal .actions{position:absolute;left:0;right:0;bottom:0;height:27px;border-top:1px solid var(--line);display:flex;font-size:8.5px}
.modal .actions span{flex:1;display:flex;align-items:center;justify-content:center}
.modal .actions .no{color:var(--red);border-right:1px solid var(--line)}
.modal .actions .yes{color:var(--blue)}
</style>
</head>
<body>

<!-- 1 Book a vehicle -->
<section class="screen row-top c1">
  <div class="status"><span>●●●●○ NORD</span><span class="time">4:21 PM</span><span>22% ▭</span></div>
  <div class="photo" style="height:201px;background:var(--photo-dash)" role="img" aria-label="Photo of a car dashboard with steering wheel"></div>
  <div class="round-btn"><svg width="10" height="8" viewBox="0 0 10 8"><path d="M0 1h10M0 4h10M0 7h10" stroke="#fff" stroke-width="1.2"/></svg></div>
  <div class="card book-card">
    <h2>Book a Vehicle</h2>
    <div class="rule"></div>
    <div class="label">DATE</div>
    <div class="value" style="margin-top:3px">20 January 2016</div>
    <div class="rule" style="margin:7px 10px"></div>
    <div class="label">TIME</div>
    <div class="split"><div><div class="cap">TIME</div><div class="v">08.00 AM</div></div><div><div class="cap">DURATION</div><div class="v">08.00 AM</div></div></div>
  </div>
  <div class="pill teal" style="top:331px">SEARCH</div>
</section>

<!-- 2 Search results -->
<section class="screen row-top c2">
  <div class="appbar">
    <div class="status"><span>●●●●○ NORD</span><span class="time">4:21 PM</span><span>22% ▭</span></div>
    <svg class="icon" style="left:8px;top:20px" width="8" height="12" viewBox="0 0 8 12"><path d="M7 1 2 6l5 5" fill="none" stroke="#fff" stroke-width="1.4"/></svg>
    <div class="sub" style="top:13px">20 January 2017</div>
    <div class="sub" style="top:25px">08.00 AM &nbsp;—&nbsp; 3 Hours</div>
    <svg class="icon" style="right:9px;top:18px" width="14" height="14" viewBox="0 0 14 14"><path d="M1 1h12L8.5 7v6L5.5 11V7z" fill="none" stroke="#fff" stroke-width="1.1"/></svg>
  </div>
  <div class="car-row" style="top:49px"><div class="thumb" role="img" aria-label="Photo of a dark hatchback"></div><div class="info"><div class="name">Arvo AAA</div><div class="meta">Comp : FREE</div></div><div class="avail">AVAILABLE NOW</div><div class="mini drive">DRIVE</div></div>
  <div class="car-row" style="top:118px"><div class="thumb" role="img" aria-label="Photo of a dark hatchback"></div><div class="info"><div class="name">Arvo AAA</div><div class="meta">Comp : FREE</div></div><div class="avail">AVAILABLE NOW</div><div class="mini drive">DRIVE</div></div>
  <div class="car-row" style="top:187px"><div class="thumb" role="img" aria-label="Photo of a dark hatchback"></div><div class="info"><div class="name">Arvo AAA</div><div class="meta">Comp : FREE</div></div><div class="mini book">BOOK</div></div>
  <div class="car-row" style="top:256px"><div class="thumb" role="img" aria-label="Photo of a dark hatchback"></div><div class="info"><div class="name">Arvo AAA</div><div class="meta">Comp : FREE</div></div><div class="mini book">BOOK</div></div>
  <div class="car-row" style="top:325px"><div class="thumb" role="img" aria-label="Photo of a dark hatchback"></div><div class="info"><div class="name">Arvo AAA</div><div class="meta">Comp : FREE</div></div></div>
</section>

<!-- 3 Car detail -->
<section class="screen row-top c3">
  <div class="status"><span>●●●●○ NORD</span><span class="time">4:21 PM</span><span>22% ▭</span></div>
  <div class="photo" style="height:205px;background:var(--photo-car)" role="img" aria-label="Photo of a dark hatchback under a cloudy sky"></div>
  <div class="round-btn"><svg width="7" height="10" viewBox="0 0 7 10"><path d="M6 1 2 5l4 4" fill="none" stroke="#fff" stroke-width="1.4"/></svg></div>
  <div class="dots"><i></i><i></i><i></i><i></i></div>
  <div class="card detail-card">
    <div class="head"><div><div class="nm">Arvo AAA</div><div class="sr">Arvo AAA Z Series</div></div><div><div class="pr">$75</div><div class="hr">3 hours</div></div></div>
    <div class="specs">
      <span><svg width="8" height="8" viewBox="0 0 8 8"><circle cx="4" cy="2.3" r="2" fill="var(--teal)"/><path d="M0 8a4 3 0 0 1 8 0z" fill="var(--teal)"/></svg>4</span>
      <span><svg width="8" height="8"><circle cx="4" cy="4" r="4" fill="var(--teal)"/></svg>Manual</span>
      <span><svg width="8" height="8"><rect x="1" y="0" width="6" height="8" rx="1" fill="var(--teal)"/></svg>D</span>
      <span><svg width="8" height="8" viewBox="0 0 8 8"><path d="M4 0v8M0 4h8M1 1l6 6M7 1 1 7" stroke="var(--teal)" stroke-width="1"/></svg>A/C</span>
    </div>
    <p>Lorem ipsum dolor sit amet, consectetur adipisicing elit, sed do eiusmod tempor incididunt ut labore et dolore magna aliqua. Ut enim ad minim veniam, quis nostrud exercitation ullamco laboris nisi ut</p>
  </div>
  <div class="pill teal" style="top:331px">RENT CAR</div>
</section>

<!-- 4 Active reservation -->
<section class="screen row-top c4">
  <div class="status"><span>●●●●○ NORD</span><span class="time">4:21 PM</span><span>22% ▭</span></div>
  <div class="photo" style="height:200px;background:var(--photo-car)" role="img" aria-label="Photo of a dark hatchback under a cloudy sky"></div>
  <div class="round-btn"><svg width="10" height="8" viewBox="0 0 10 8"><path d="M0 1h10M0 4h10M0 7h10" stroke="#fff" stroke-width="1.2"/></svg></div>
  <div class="card active-card">
    <div class="nm">Arvo AAA</div>
    <div class="rem">Remaining:<br>1 hour 25 min 13 sec</div>
    <div class="lock close"><svg width="9" height="10" viewBox="0 0 9 10"><path d="M2 4.5V3a2.5 2.5 0 0 1 5 0v1.5" fill="none" stroke="#fff" stroke-width="1.1"/><rect x="1" y="4.5" width="7" height="5" rx="1" fill="none" stroke="#fff" stroke-width="1.1"/></svg></div>
    <div class="lock open"><svg width="9" height="10" viewBox="0 0 9 10"><path d="M2 4.5V3a2.5 2.5 0 0 1 5 0" fill="none" stroke="#fff" stroke-width="1.1"/><rect x="1" y="4.5" width="7" height="5" rx="1" fill="none" stroke="#fff" stroke-width="1.1"/></svg></div>
    <div class="loc">LOCATION</div>
    <div class="map" role="img" aria-label="Street map showing the car's location"></div>
    <svg style="position:absolute;left:87px;top:90px" width="11" height="15" viewBox="0 0 11 15"><path d="M5.5 15S0 8.5 0 5.5a5.5 5.5 0 0 1 11 0C11 8.5 5.5 15 5.5 15z" fill="#ee5a2c"/><circle cx="5.5" cy="5.5" r="2" fill="#fff"/></svg>
  </div>
  <div class="pill red" style="top:331px">END RESERVATION</div>
</section>

<!-- 5 History -->
<section class="screen row-top c5">
  <div class="appbar">
    <div class="status"><span>●●●●○ NORD</span><span class="time">4:21 PM</span><span>22% ▭</span></div>
    <svg class="icon" style="left:9px;top:21px" width="12" height="9" viewBox="0 0 12 9"><path d="M0 1h12M0 4.5h12M0 8h12" stroke="#fff" stroke-width="1.1"/></svg>
    <div class="title">History</div>
  </div>
  <div class="car-row" style="top:49px"><div class="thumb" role="img" aria-label="Photo of a dark hatchback"></div><div class="info"><div class="date">20 January 2017 8:00AM</div><div class="name">Arvo AAA</div><div class="meta">2 hours 40 mins</div></div><div class="tag ongoing">ON GOING</div></div>
  <div class="car-row" style="top:118px"><div class="thumb" role="img" aria-label="Photo of a dark hatchback"></div><div class="info"><div class="date">20 January 2017 8:00AM</div><div class="name">Arvo AAA</div><div class="meta">2 hours 40 mins</div></div><div class="tag complete">COMPLETE</div></div>
  <div class="car-row" style="top:187px"><div class="thumb" role="img" aria-label="Photo of a dark hatchback"></div><div class="info"><div class="date">20 January 2017 8:00AM</div><div class="name">Arvo AAA</div><div class="meta">2 hours 40 mins</div></div><div class="tag canceled">CANCELED</div></div>
</section>

<!-- 6 Menu -->
<section class="screen row-bottom c1">
  <div class="drawer-shade" role="img" aria-label="Dimmed active reservation screen behind the menu"></div>
  <div style="position:absolute;left:168px;top:165px;width:20px;height:20px;border-radius:50%;background:#2f7d3a"></div>
  <div class="drawer">
    <div class="avatar" role="img" aria-label="Profile photo of the driver"></div>
    <div class="profile-name">Milo Hart</div>
    <div class="profile-link">VIEW PROFILE</div>
    <div class="rule"></div>
    <div class="menu-item on" style="top:128px"><svg viewBox="0 0 11 11"><rect x="1" y="2" width="9" height="8" rx="1" fill="none" stroke="currentColor"/><path d="M1 4.5h9M3.5 1v2M7.5 1v2" stroke="currentColor"/></svg>Book</div>
    <div class="menu-item" style="top:157px"><svg viewBox="0 0 11 11"><rect x="1" y="1" width="8" height="9" fill="none" stroke="currentColor"/><path d="M3 4h4M3 6h4M6 10l4-5" stroke="currentColor"/></svg>My Reservation</div>
    <div class="menu-item" style="top:186px"><svg viewBox="0 0 11 11"><path d="M1 7V5l1.5-3h6L10 5v2z" fill="currentColor"/><circle cx="3" cy="8.5" r="1.2" fill="currentColor"/><circle cx="8" cy="8.5" r="1.2" fill="currentColor"/></svg>Drive</div>
    <div class="menu-item" style="top:215px"><svg viewBox="0 0 11 11"><path d="M2 1h7M2 10h7M3 1c0 3 5 3 5 4.5S3 7 3 10M8 1c0 3-5 3-5 4.5S8 7 8 10" fill="none" stroke="currentColor"/></svg>History</div>
    <div class="menu-item" style="top:244px"><svg viewBox="0 0 11 11"><circle cx="4" cy="7" r="2.6" fill="none" stroke="currentColor" stroke-width="1.4"/><circle cx="8.5" cy="2.5" r="1.6" fill="none" stroke="currentColor"/></svg>Settings</div>
  </div>
</section>

<!-- 7 My reservations -->
<section class="screen row-bottom c2">
  <div class="appbar">
    <div class="status"><span>●●●●○ NORD</span><span class="time">4:21 PM</span><span>22% ▭</span></div>
    <svg class="icon" style="left:9px;top:21px" width="12" height="9" viewBox="0 0 12 9"><path d="M0 1h12M0 4.5h12M0 8h12" stroke="#fff" stroke-width="1.1"/></svg>
    <div class="title">My Reservation</div>
  </div>
  <div class="car-row" style="top:51px"><div class="thumb" role="img" aria-label="Photo of a dark hatchback"></div><div class="info"><div class="date">20 January 2017 8:00AM</div><div class="name">Arvo AAA</div><div class="meta">2 hours 40 mins</div><div class="price">$ 80</div></div></div>
  <div class="swipe-actions" style="top:120px">
    <div class="swipe-card"><div class="car-row" style="all:unset"><div class="date" style="font-size:6px;color:var(--muted);margin-bottom:3px">20 January 2017 8:00AM</div><div style="font-size:8.5px;font-weight:500">Arvo AAA</div><div style="font-size:6px;color:var(--muted);margin-top:1px">2 hours 40 mins</div><div style="font-size:8.5px;font-weight:500;margin-top:2px">$ 80</div></div></div>
    <div class="act" style="left:136px;color:var(--orange)"><svg width="11" height="11" viewBox="0 0 11 11"><path d="M1 10l.6-2.8L8 .8l2.2 2.2L3.8 9.4z" fill="none" stroke="currentColor"/></svg>Edit</div>
    <div class="act" style="left:168px;color:var(--red)"><svg width="11" height="11" viewBox="0 0 11 11"><path d="M1.5 2.5h8M4 2.5V1h3v1.5M2.5 2.5l.7 8h4.6l.7-8M4.5 4.5v4M6.5 4.5v4" fill="none" stroke="currentColor"/></svg>Delete</div>
  </div>
  <div class="car-row" style="top:189px"><div class="thumb" role="img" aria-label="Photo of a dark hatchback"></div><div class="info"><div class="date">20 January 2017 8:00AM</div><div class="name">Arvo AAA</div><div class="meta">2 hours 40 mins</div><div class="price">$ 80</div></div></div>
</section>

<!-- 8 Payment -->
<section class="screen row-bottom c3">
  <div class="pay-head">
    <div class="status"><span>●●●●○ NORD</span><span class="time">4:21 PM</span><span>22% ▭</span></div>
    <span class="cancel">Cancel</span><span class="title">Payment</span>
  </div>
  <div class="pay-body">
    <h3>Select Payment Method</h3>
    <div class="tile selected" style="left:9px;top:32px"><div class="art" style="background:linear-gradient(135deg,#bfe0f2,#7fb6d8)" role="img" aria-label="Illustration of a personal bank card"></div>My Card<small>9825 0283 XXXX</small></div>
    <div class="tile" style="left:107px;top:32px"><div class="art" style="background:linear-gradient(180deg,#3a3f48 0 30%,#e8eaec 30%)" role="img" aria-label="Illustration of a company card"></div>Company Card<small>9825 0283 XXXX</small></div>
    <div class="tile" style="left:9px;top:104px"><svg style="display:block;margin:14px auto 8px" width="22" height="22" viewBox="0 0 22 22"><path d="M11 1v20M1 11h20" stroke="var(--blue)" stroke-width="1.6"/></svg>Add New Card</div>
  </div>
</section>

<!-- 9 Confirm (until) -->
<section class="screen row-bottom c4">
  <div class="appbar">
    <div class="status"><span>●●●●○ NORD</span><span class="time">4:21 PM</span><span>22% ▭</span></div>
    <svg class="icon" style="left:8px;top:20px" width="8" height="12" viewBox="0 0 8 12"><path d="M7 1 2 6l5 5" fill="none" stroke="#fff" stroke-width="1.4"/></svg>
    <div class="sub" style="top:13px">20 January 2017</div>
    <div class="sub" style="top:25px">08.00 AM &nbsp;—&nbsp; 3 Hours</div>
    <svg class="icon" style="right:9px;top:18px" width="14" height="14" viewBox="0 0 14 14"><path d="M1 1h12L8.5 7v6L5.5 11V7z" fill="none" stroke="#fff" stroke-width="1.1"/></svg>
  </div>
  <div class="car-row" style="top:49px"><div class="thumb" role="img" aria-label="Photo of a dark hatchback"></div></div>
  <div class="car-row" style="top:118px"><div class="thumb" role="img" aria-label="Photo of a dark hatchback"></div></div>
  <div class="car-row" style="top:187px"><div class="thumb" role="img" aria-label="Photo of a dark hatchback"></div></div>
  <div class="car-row" style="top:256px"><div class="thumb" role="img" aria-label="Photo of a dark hatchback"></div><div class="info"><div class="name">Arvo AAA</div><div class="meta">Comp : FREE</div></div><div class="mini book">BOOK</div></div>
  <div class="car-row" style="top:325px"><div class="thumb" role="img" aria-label="Photo of a dark hatchback"></div><div class="info"><div class="name">Arvo AAA</div><div class="meta">Comp : FREE</div></div></div>
  <div class="scrim"></div>
  <div class="modal" style="top:59px;height:189px">
    <div class="lead">You are reserving</div>
    <div class="carpic" role="img" aria-label="Round photo of the reserved car"></div>
    <div class="nm">Arvo AAA</div>
    <div class="phase">Until</div>
    <div class="dt"><div><div class="cap">DATE</div><div class="v">18 January 2017</div></div><div style="flex:.7"><div class="cap">TIME</div><div class="v">11.00 AM</div></div></div>
    <div class="actions"><span class="no">Cancel</span><span class="yes">Confirm and Drive</span></div>
  </div>
</section>

<!-- 10 Confirm (from / until) -->
<section class="screen row-bottom c5">
  <div class="appbar">
    <div class="status"><span>●●●●○ NORD</span><span class="time">4:21 PM</span><span>22% ▭</span></div>
    <svg class="icon" style="left:8px;top:20px" width="8" height="12" viewBox="0 0 8 12"><path d="M7 1 2 6l5 5" fill="none" stroke="#fff" stroke-width="1.4"/></svg>
    <div class="sub" style="top:13px">20 January 2017</div>
    <div class="sub" style="top:25px">08.00 AM &nbsp;—&nbsp; 3 Hours</div>
    <svg class="icon" style="right:9px;top:18px" width="14" height="14" viewBox="0 0 14 14"><path d="M1 1h12L8.5 7v6L5.5 11V7z" fill="none" stroke="#fff" stroke-width="1.1"/></svg>
  </div>
  <div class="car-row" style="top:49px"><div class="thumb" role="img" aria-label="Photo of a dark hatchback"></div></div>
  <div class="car-row" style="top:118px"><div class="thumb" role="img" aria-label="Photo of a dark hatchback"></div></div>
  <div class="car-row" style="top:187px"><div class="thumb" role="img" aria-label="Photo of a dark hatchback"></div></div>
  <div class="car-row" style="top:256px"><div class="thumb" role="img" aria-label="Photo of a dark hatchback"></div><div class="info"><div class="name">Arvo AAA</div><div class="meta">Comp : FREE</div></div><div class="mini book">BOOK</div></div>
  <div class="car-row" style="top:325px"><div class="thumb" role="img" aria-label="Photo of a dark hatchback"></div><div class="info"><div class="name">Arvo AAA</div><div class="meta">Comp : FREE</div></div></div>
  <div class="scrim"></div>
  <div class="modal" style="top:59px;height:233px">
    <div class="lead">You are reserving</div>
    <div class="carpic" role="img" aria-label="Round photo of the reserved car"></div>
    <div class="nm">Arvo AAA</div>
    <div class="phase">From</div>
    <div class="dt"><div><div class="cap">DATE</div><div class="v">18 January 2017</div></div><div style="flex:.7"><div class="cap">TIME</div><div class="v">8.00 AM</div></div></div>
    <div class="phase">Until</div>
    <div class="dt"><div><div class="cap">DATE</div><div class="v">18 January 2017</div></div><div style="flex:.7"><div class="cap">TIME</div><div class="v">11.00 AM</div></div></div>
    <div class="actions"><span class="no">Cancel</span><span class="yes">Confirm and Drive</span></div>
  </div>
</section>

</body>
</html>
```